LETTERHEAD & ENVELOPE: eye-catching stationary design for our custom office furniture business

Our company recently rebranded and we are in need of new stationary. Specifically, we need branded letterhead for standard paper size (8.5” x 11”), and matching envelopes, size: #9.

All designs should incorporate our brand colors, brand typeface, and logo. Please view attached brand guidelines document for brand colors, and brand description.

Letterhead: 8.5” x 11” Must include CoralvexKTN Logo, Dorrit Falke Certified Dealer Logo, mailing address, phone number, website, and email address.

Envelope: 9.5” x 4.125” Must include CoralvexKTN Logo, mailing address, and Dorrit Falke Certified Dealer Logo.

Attached files include:

```html
<!DOCTYPE html>
<html lang="en">
<head>
<meta charset="utf-8">
<title>CoralvexKTN Stationery</title>
<link href="https://fonts.googleapis.com/css2?family=Fira+Sans:wght@300;400&family=Raleway:wght@400&display=swap" rel="stylesheet">
<style>
  :root {
    --backdrop: #cccccc;
    --paper: #f8f9f8;
    --brand-green: #4a7265;
    --text-grey: #9a9a9a;
    --text-dark: #5a5a5a;
    --dealer-red: #e0452e;
    --peach: #f0c7b5;
  }
  * { margin: 0; padding: 0; box-sizing: border-box; }
  html, body { width: 1200px; height: 828px; overflow: hidden; background: var(--backdrop); }
  body { position: relative; font-family: "Fira Sans", sans-serif; color: var(--text-grey); }

  .sheet { position: absolute; background: var(--paper); }
  .letterhead { left: 94px; top: 119px; width: 455px; height: 588px; }
  .envelope-front { left: 610px; top: 158px; width: 495px; height: 220px; overflow: hidden; }
  .envelope-back { left: 610px; top: 409px; width: 495px; height: 220px; overflow: hidden; }

  .brand { position: absolute; display: flex; align-items: center; }
  .brand-dot { border-radius: 50%; background: var(--brand-green); flex: none; }
  .brand-name { font-family: "Raleway", sans-serif; font-weight: 400; color: var(--brand-green); line-height: 1; white-space: nowrap; }
  .letterhead .brand { right: 35px; top: 39px; }
  .letterhead .brand-dot { width: 36px; height: 36px; margin-right: 12px; }
  .letterhead .brand-name { font-size: 28px; }
  .envelope-front .brand { left: 33px; top: 36px; }
  .envelope-front .brand-dot { width: 28px; height: 28px; margin-right: 10px; }
  .envelope-front .brand-name { font-size: 23px; }

  .salutation { position: absolute; left: 34px; top: 116px; font-size: 6.4px; font-weight: 300; }
  .letter-body { position: absolute; left: 34px; top: 152px; width: 387px; font-size: 6.35px; font-weight: 300; line-height: 12.8px; text-align: justify; letter-spacing: 0.05px; }
  .letter-body p + p { margin-top: 12.8px; }

  .sign-off { position: absolute; left: 34px; top: 385px; font-size: 6.4px; font-weight: 300; }
  .signature { position: absolute; left: 34px; top: 403px; width: 92px; height: 20px; background: linear-gradient(90deg, rgba(74,114,101,0.18), rgba(74,114,101,0.06)); border-radius: 3px; }
  .sign-title { position: absolute; left: 34px; top: 436px; font-size: 6.4px; font-weight: 300; }

  .footer-rule { position: absolute; left: 34px; top: 515px; width: 250px; height: 1px; background: linear-gradient(90deg, #a9c5bb, #dde3df 45%, var(--peach)); }

  .dealer { position: absolute; display: flex; align-items: center; white-space: nowrap; }
  .dealer-dot { width: 18px; height: 18px; border-radius: 50%; background: var(--dealer-red); margin-right: 6px; flex: none; }
  .dealer-name { font-size: 8.4px; font-weight: 300; color: var(--dealer-red); }
  .letterhead .dealer { right: 35px; top: 506px; }
  .envelope-front .dealer { right: 28px; top: 178px; }

  .contact { position: absolute; top: 538px; font-size: 7px; font-weight: 400; color: var(--text-dark); line-height: 9.6px; white-space: nowrap; }
  .contact-icons { position: absolute; top: 538px; display: flex; flex-direction: column; }
  .contact-icons svg { width: 8px; height: 9.6px; }
  .icons-phone { left: 34px; }
  .text-phone { left: 50px; }
  .icons-web { left: 140px; }
  .text-web { left: 153px; }
  .icons-address { left: 311px; }
  .text-address { left: 324px; }
  .divider { position: absolute; top: 536px; width: 1px; height: 24px; background: linear-gradient(var(--peach), #f5ddd2); }
  .divider-one { left: 117px; }
  .divider-two { left: 284px; }

  .envelope-address { position: absolute; left: 31px; top: 183px; display: flex; align-items: center; font-size: 6.8px; color: var(--text-dark); white-space: nowrap; }
  .envelope-address svg { width: 8px; height: 9px; margin-right: 7px; }

  .envelope-band { position: absolute; left: 0; bottom: 0; width: 495px; height: 16px; }
  .envelope-flap { position: absolute; left: 0; top: 0; width: 495px; height: 62px; }
  .flap-web { position: absolute; left: 0; top: 27px; width: 495px; text-align: center; font-size: 7px; letter-spacing: 1.2px; color: #e6ece9; }
</style>
</head>
<body>

<section class="sheet letterhead">
  <div class="brand"><span class="brand-dot"></span><span class="brand-name">CoralvexKTN</span></div>

  <p class="salutation">Dear Sir,</p>

  <div class="letter-body">
    <p>Lorem Ipsum is simply dummy text of the printing and typesetting industry. Lorem Ipsum has been the industry's standard dummy text ever since the 1500s, when an unknown printer took a galley of type and scrambled it to make a type specimen book. It has survived not only five centuries, but also the leap into electronic typesetting, remaining essentially unchanged. It was popularised in the 1960s with the release of Velmark sheets containing Lorem Ipsum passages, and more recently with desktop publishing software like Quillset Layout including versions of Lorem Ipsum.</p>
    <p>Lorem Ipsum is simply dummy text of the printing and typesetting industry. Lorem Ipsum has been the industry's standard dummy text ever since the 1500s, when an unknown printer took a galley of type and scrambled it to make a type specimen book. It has survived not only five centuries, but also the leap into electronic typesetting, remaining essentially unchanged. It was popularised in the 1960s with the release of Velmark sheets containing Lorem Ipsum passages, and more recently with desktop publishing software like Quillset Layout including versions of Lorem Ipsum.</p>
    <p>Lorem Ipsum is simply dummy text of the printing and typesetting industry. Lorem Ipsum has been the industry's standard dummy text ever since the 1500s, when an unknown printer took a galley of type and scrambled it to make a type specimen book.</p>
  </div>

  <p class="sign-off">Your Name</p>
  <div class="signature" role="img" aria-label="Handwritten signature"></div>
  <p class="sign-title">CEO &nbsp;|&nbsp; Owner</p>

  <div class="footer-rule"></div>
  <div class="dealer"><span class="dealer-dot"></span><span class="dealer-name">Dorrit Falke Certified Dealer</span></div>

  <div class="contact-icons icons-phone">
    <svg viewBox="0 0 8 10"><path d="M2 2.5 Q1 5.5 4 8 L5.3 6.8 L4.3 5.8 L3.6 6.3 Q2.7 5.2 3 3.9 L3.9 3.7 L3.6 2.3 Z" fill="#5a5a5a"/></svg>
    <svg viewBox="0 0 8 10"><path d="M1 4 Q4 2 7 4 L6.5 5 L5.5 4.6 L5.5 4 Q4 3.5 2.5 4 L2.5 4.6 L1.5 5 Z M2 5.5 H6 L6.5 8 H1.5 Z" fill="#5a5a5a"/></svg>
  </div>
  <p class="contact text-phone">555.214.3806<br>555.000.0000</p>
  <div class="divider divider-one"></div>

  <div class="contact-icons icons-web">
    <svg viewBox="0 0 8 10"><rect x="0.8" y="2.8" width="6.4" height="4.4" fill="#5a5a5a"/><path d="M0.8 2.8 L4 5.2 L7.2 2.8" stroke="#f8f9f8" stroke-width="0.7" fill="none"/></svg>
    <svg viewBox="0 0 8 10"><circle cx="4" cy="5" r="3" fill="none" stroke="#5a5a5a" stroke-width="0.8"/><ellipse cx="4" cy="5" rx="1.2" ry="3" fill="none" stroke="#5a5a5a" stroke-width="0.6"/><line x1="1" y1="5" x2="7" y2="5" stroke="#5a5a5a" stroke-width="0.6"/></svg>
  </div>
  <p class="contact text-web">Lena_Ostrow@coralvexktn.com<br>www.coralvexktn.com</p>
  <div class="divider divider-two"></div>

  <div class="contact-icons icons-address">
    <svg viewBox="0 0 8 10"><path d="M4 1 A2.8 2.8 0 0 1 6.8 3.8 Q6.8 5.5 4 8.5 Q1.2 5.5 1.2 3.8 A2.8 2.8 0 0 1 4 1 Z" fill="#4a7265"/><circle cx="4" cy="3.8" r="1" fill="#f8f9f8"/></svg>
  </div>
  <p class="contact text-address">410 SW Alderbrook, Suite 120<br>Portland, OR 97201</p>
</section>

<section class="sheet envelope-front">
  <div class="brand"><span class="brand-dot"></span><span class="brand-name">CoralvexKTN</span></div>
  <div class="envelope-address">
    <svg viewBox="0 0 8 10"><path d="M4 1 A2.8 2.8 0 0 1 6.8 3.8 Q6.8 5.5 4 8.5 Q1.2 5.5 1.2 3.8 A2.8 2.8 0 0 1 4 1 Z" fill="#5a5a5a"/><circle cx="4" cy="3.8" r="1" fill="#f8f9f8"/></svg>
    410 SW Alderbrook, Suite 120 Portland, OR 97201
  </div>
  <div class="dealer"><span class="dealer-dot"></span><span class="dealer-name">Dorrit Falke Certified Dealer</span></div>
  <svg class="envelope-band" viewBox="0 0 495 16" preserveAspectRatio="none">
    <path d="M0 9 H308 Q318 9 322 5 Q327 1 340 1 H495 V16 H0 Z" fill="#4a7265"/>
  </svg>
</section>

<section class="sheet envelope-back">
  <svg class="envelope-flap" viewBox="0 0 495 62" preserveAspectRatio="none">
    <path d="M0 0 H495 L480 52 Q477 60 465 60 H30 Q18 60 15 52 Z" fill="#4a7265"/>
  </svg>
  <p class="flap-web">www.coralvexktn.com</p>
</section>

</body>
</html>
```